Flyer design for carpet cleaning

We want to design a flyer for our new wing of business. Carpet and upholstery cleaning. We want it to match with the previous branding so please refer out website. Www.brivelcora.co.uk and see the carpet section. We currently have 4 services
Carpet and rug (cleaning and stain protection coating)
Upholstery and curtain (cleaning and stain protection coating)
Floor and patio (cleaning and polishing)
Antimicrobial (90 days self disinfecting coating)
Our price list is on the website I will attach some qr codes that I would like to put on the website.
Please use these terms
- quickest dry time
-24 hours call out
-based in London
-100% satisfaction guaranteed
-Low moisture cleaning
-Nano technology based stain protectant
- long lasting antimicrobial protection
Adding photos or not adding is designer choice and even putting price list or not is designer choice. The prices can be starting from format or full price list at the back page and other details in front

```html
<!DOCTYPE html>
<html lang="en">
<head>
<meta charset="utf-8">
<title>Brivelcora – Carpet, Upholstery, Curtain &amp; Flooring</title>
<link href="https://fonts.googleapis.com/css2?family=Archivo+Narrow:wght@400;700&family=Libre+Franklin:wght@600;800&family=PT+Sans&family=Tinos&display=swap" rel="stylesheet">
<style>
  :root {
    --royal: #1c5ff0;
    --aqua: #45d6ea;
    --mint: #7ff7e4;
    --brand-blue: #2a8ee2;
    --ink: #0b0b0b;
    --white: #ffffff;
    --bullet: #f2a20c;
  }
  * { margin: 0; padding: 0; box-sizing: border-box; }
  html, body { width: 846px; height: 1200px; overflow: hidden; background: var(--white); }
  .flyer { position: relative; width: 846px; height: 1200px; background: var(--aqua); overflow: hidden; }

  .header-band { position: absolute; left: 0; top: 0; width: 571px; height: 218px; background: var(--royal); }
  .header-band .trades {
    position: absolute; left: 55px; top: 104px;
    font-family: "PT Sans", sans-serif; font-size: 23px; letter-spacing: 1.6px; color: var(--white);
  }

  .brand-panel { position: absolute; left: 571px; top: 0; width: 275px; height: 218px; background: var(--white); text-align: center; }
  .brand-panel .brand-name {
    position: absolute; left: 0; right: 0; top: 116px;
    font-family: "Libre Franklin", sans-serif; font-weight: 600; font-size: 29px; color: var(--brand-blue);
  }
  .brand-panel .brand-tagline {
    position: absolute; left: 0; right: 0; top: 152px;
    font-family: "Libre Franklin", sans-serif; font-weight: 600; font-size: 12px; color: var(--royal);
  }

  .services { position: absolute; left: 28px; top: 272px; list-style: none; }
  .service { position: relative; padding-left: 22px; margin-bottom: 6px; }
  .service::before {
    content: ""; position: absolute; left: 0; top: 12px; width: 14px; height: 14px; background: var(--bullet);
  }
  .service-title { font-family: "Libre Franklin", sans-serif; font-weight: 800; font-size: 27px; line-height: 40px; color: var(--ink); }
  .service-detail { font-family: "Archivo Narrow", sans-serif; font-size: 29px; line-height: 38px; color: var(--white); }

  .photo { position: absolute; left: 571px; width: 275px; }
  .photo-sofa { top: 221px; height: 208px; background: linear-gradient(135deg, #d9b9a9, #c69f90 55%, #e9dcd5); }
  .photo-carpet { top: 438px; height: 266px; background: linear-gradient(160deg, #e8ddd3, #cbbdb0 60%, #ddd1c6); }
  .photo-sprayer { top: 713px; height: 206px; background: linear-gradient(120deg, #b78a55, #d9c8b2 50%, #8d6b45); }
  .photo-suit { top: 927px; height: 206px; background: linear-gradient(140deg, #9aa8a6, #e4e6e3 50%, #6c6a62); }
  .footer-band { position: absolute; left: 571px; top: 1133px; width: 275px; height: 67px; background: var(--royal); }

  .features { position: absolute; left: 24px; top: 679px; list-style: none; }
  .feature { position: relative; height: 66px; width: 580px; }
  .feature .band {
    position: absolute; left: 60px; top: 14px; width: 520px; height: 34px; background: var(--mint);
  }
  .feature .label {
    position: absolute; left: 78px; top: 14px; line-height: 34px;
    font-family: "Tinos", serif; font-size: 25px; color: var(--ink);
  }
  .feature .icon-box {
    position: absolute; left: 0; top: 0; width: 64px; height: 62px;
    background: var(--mint); border: 1.5px solid var(--ink); border-radius: 9px;
    display: flex; align-items: center; justify-content: center;
  }
  .icon-box svg { width: 40px; height: 40px; }
  .icon-24 { font-family: "Archivo Narrow", sans-serif; font-size: 38px; letter-spacing: -3px; color: var(--ink); }
</style>
</head>
<body>
<main class="flyer">
  <header class="header-band">
    <p class="trades">CARPET • UPHOLSTERY • CURTAIN &amp; FLOORING</p>
  </header>

  <div class="brand-panel">
    <p class="brand-name">Brivelcora</p>
    <p class="brand-tagline">Nano enhanced cleaning and coating</p>
  </div>

  <ul class="services">
    <li class="service"><p class="service-title">Carpet and rug</p><p class="service-detail">(Cleaning and stain protection coating)</p></li>
    <li class="service"><p class="service-title">Upholstery and curtain</p><p class="service-detail">(Cleaning and stain protection coating)</p></li>
    <li class="service"><p class="service-title">Floor and patio</p><p class="service-detail">(cleaning and polishing)</p></li>
    <li class="service"><p class="service-title">Antimicrobial</p><p class="service-detail">(90 days self disinfecting coating)</p></li>
  </ul>

  <div class="photo photo-sofa" role="img" aria-label="Gloved hand cleaning a pink sofa with an upholstery extraction tool"></div>
  <div class="photo photo-carpet" role="img" aria-label="Carpet extraction wand cleaning a beige carpet"></div>
  <div class="photo photo-sprayer" role="img" aria-label="Gloved hands holding a disinfecting fogger"></div>
  <div class="photo photo-suit" role="img" aria-label="Technician in protective suit spraying a living room"></div>
  <div class="footer-band"></div>

  <ul class="features">
    <li class="feature"><span class="band"></span><span class="label">Quickest dry time</span>
      <span class="icon-box"><svg viewBox="0 0 40 40"><path d="M6 10 L20 20 L6 30 Z M20 10 L34 20 L20 30 Z" fill="none" stroke="#0b0b0b" stroke-width="3" stroke-linejoin="round"/></svg></span></li>
    <li class="feature"><span class="band"></span><span class="label">24 hours call out</span>
      <span class="icon-box"><span class="icon-24">24</span></span></li>
    <li class="feature"><span class="band"></span><span class="label">Based in London</span>
      <span class="icon-box"><svg viewBox="0 0 40 40"><path d="M20 6 C13 6 9 11 9 16 C9 24 20 34 20 34 C20 34 31 24 31 16 C31 11 27 6 20 6 Z" fill="none" stroke="#0b0b0b" stroke-width="2.5"/><circle cx="20" cy="16" r="4" fill="#0b0b0b"/></svg></span></li>
    <li class="feature"><span class="band"></span><span class="label">100% satisfaction guaranteed</span>
      <span class="icon-box"><svg viewBox="0 0 40 40"><path d="M9 21 L17 29 L32 12" fill="none" stroke="#0b0b0b" stroke-width="3.5" stroke-linecap="round" stroke-linejoin="round"/></svg></span></li>
    <li class="feature"><span class="band"></span><span class="label">Low moisture cleaning</span>
      <span class="icon-box"><svg viewBox="0 0 40 40"><g stroke="#0b0b0b" stroke-width="2.5" stroke-linecap="round"><path d="M20 23 V33 M15 28 H25 M16.5 24.5 L23.5 31.5 M23.5 24.5 L16.5 31.5"/></g></svg></span></li>
    <li class="feature"><span class="band"></span><span class="label">Nano technology based stain protectant</span>
      <span class="icon-box"><svg viewBox="0 0 40 40"><path d="M14 6 H26 L20 15 Z" fill="#0b0b0b"/><g stroke="#0b0b0b" stroke-width="1.5"><path d="M2 22 H38 M2 26 H38 M2 30 H38 M2 34 H38"/></g></svg></span></li>
    <li class="feature"><span class="band"></span><span class="label">Long lasting antimicrobial protection</span>
      <span class="icon-box"><svg viewBox="0 0 40 40"><g stroke="#0b0b0b" stroke-width="2.5" stroke-linecap="round" fill="none"><path d="M20 5 V35 M7 12.5 L33 27.5 M7 27.5 L33 12.5"/><path d="M16 8 L20 11 L24 8 M16 32 L20 29 L24 32 M8 17 L12 15 L11 11 M32 23 L28 25 L29 29 M8 23 L12 25 L11 29 M32 17 L28 15 L29 11"/></g></svg></span></li>
  </ul>
</main>
</body>
</html>
```